Word Doc Design for construction report

We have a database that dumps all of this data into this word doc. We need a much more appealing, visually friendly document. I have attached the main document and the cover page.
You don't need to edited all the repeated pages, just give us a style guide. I have attached our branding.
Updates

Hi I have pulled together a final design and now just need someone to put it all into a word doc. The final document is 36 pages. I am prepared to pay the design fee listed plus a $200 tip, however, we need it delivered by Monday. Is there anyone available to do this work?

Requirements
Must have
• Be easy on the eye as there is a LOT of repeated content

```html
<!DOCTYPE html>
<html lang="en">
<head>
<meta charset="utf-8">
<title>ACT Maintenance Plan – Report Pages</title>
<link href="https://fonts.googleapis.com/css2?family=Montserrat:wght@400;500;600;700;800&display=swap" rel="stylesheet">
<style>
  :root {
    --navy: #252f6e;
    --teal: #1ca98f;
    --blue: #1f8fd0;
    --cyan: #1b8fc9;
    --ink: #3b3b3b;
    --rule: #c9c9c9;
    --stage: #e2e2e2;
  }
  * { margin: 0; padding: 0; box-sizing: border-box; }
  html, body { width: 966px; height: 1200px; overflow: hidden; }
  body { background: var(--stage); font-family: "Montserrat", sans-serif; color: var(--ink); position: relative; }

  .page { position: absolute; width: 382px; height: 539px; background: #fff; overflow: hidden; }
  .page--cover { left: 86px; top: 45px; }
  .page--summary { left: 498px; top: 45px; }
  .page--community { left: 86px; top: 617px; }
  .page--terms { left: 498px; top: 617px; }
  .page svg.art { position: absolute; inset: 0; width: 382px; height: 539px; }
  .abs { position: absolute; }

  /* brand name */
  .brand { position: absolute; font-weight: 800; color: var(--navy); letter-spacing: 0.5px; text-align: center; }

  /* cover */
  .cover-title { left: 36px; top: 128px; font-weight: 700; font-size: 27px; line-height: 27px; }
  .cover-title .t-act { color: var(--blue); display: block; }
  .cover-title .t-main { color: var(--teal); display: block; }
  .cover-title .t-plan { color: var(--navy); display: block; }
  .cover-rule { left: 36px; top: 216px; width: 89px; height: 2px; background: var(--blue); }
  .cover-date { left: 36px; top: 225px; font-size: 13px; color: var(--navy); }
  .cover-site { right: 14px; top: 262px; text-align: right; color: #fff; font-size: 9.5px; line-height: 12px; }
  .cover-contact { top: 496px; color: #fff; font-size: 7px; line-height: 10px; }
  .cover-contact strong { font-weight: 600; }

  /* summary */
  .side-heading { color: #fff; font-weight: 800; font-size: 15.5px; line-height: 18px; left: 12px; top: 38px; }
  .side-label { font-weight: 700; font-size: 10.5px; left: 12px; }
  .side-label--scope { top: 141px; color: var(--cyan); }
  .side-label--class { top: 212px; color: var(--cyan); }
  .side-note { left: 11px; top: 227px; color: #fff; font-size: 5.4px; }
  .facts { left: 117px; width: 203px; font-size: 6.2px; }
  .facts .row { display: flex; height: 12px; align-items: flex-end; }
  .facts .k { width: 91px; font-weight: 700; color: var(--cyan); border-bottom: 0.5px solid var(--rule); padding-bottom: 1px; }
  .facts .v { flex: 1; border-bottom: 0.5px solid var(--rule); padding-bottom: 1px; margin-left: 0; }
  .facts--a { top: 7px; }
  .facts--b { top: 78px; width: 134px; }
  .facts--b .row { height: 11px; }
  .body { left: 117px; width: 252px; font-size: 5.6px; line-height: 8.9px; text-align: justify; color: #555; }
  .body--lead { top: 134px; font-size: 6.3px; line-height: 8.7px; text-align: left; }
  .bullets { left: 117px; top: 170px; width: 252px; font-size: 6.3px; display: flex; color: #555; }
  .bullets span { flex: 1; padding-left: 9px; position: relative; line-height: 8.5px; }
  .bullets span::before { content: "➲"; position: absolute; left: 0; color: var(--teal); font-size: 6px; }
  .body--class { top: 198px; }
  .body--act { top: 258px; }
  .body--file { top: 353px; }
  .important { left: 117px; top: 423px; color: var(--cyan); font-weight: 700; font-size: 9px; }
  .body--important { top: 436px; }
  .body--important em { font-weight: 600; font-style: italic; color: #333; }
  .thanks { left: 118px; top: 501px; width: 163px; font-size: 5.8px; line-height: 8px; color: #555; }
  .signoff { left: 289px; top: 517px; font-size: 5.8px; line-height: 8px; color: #555; }

  /* community */
  .charity-text { left: 50px; top: 86px; width: 115px; color: #fff; font-size: 5.9px; line-height: 8px; }
  .charity-name { left: 0; width: 382px; top: 206px; text-align: center; color: var(--teal); font-weight: 700; font-size: 15px; }
  .photo-note { left: 20px; width: 342px; top: 268px; text-align: center; font-size: 8.3px; line-height: 11px; color: #444; }

  /* terms */
  .use-heading { left: 16px; top: 218px; color: var(--cyan); font-weight: 600; font-size: 10px; line-height: 13px; }
  .use-item { left: 17px; top: 253px; width: 210px; font-size: 6.4px; line-height: 9px; color: #555; }
  .valid { left: 17px; top: 295px; font-size: 8.4px; font-weight: 600; color: #333; }
  .legal { width: 167px; font-size: 6.5px; line-height: 9.7px; text-align: justify; color: #555; }
  .legal b { font-weight: 700; color: #333; }
  .legal--l { left: 18px; }
  .legal--r { left: 197px; }
  .copyright { left: 0; width: 382px; top: 505px; text-align: center; color: var(--cyan); font-size: 6.3px; line-height: 9.5px; }
</style>
</head>
<body>

<!-- Page 1: cover -->
<section class="page page--cover">
  <svg class="art" viewBox="0 0 382 539" aria-hidden="false">
    <defs>
      <linearGradient id="bldg" x1="0" y1="0" x2="0" y2="1">
        <stop offset="0" stop-color="#7b97c7"/>
        <stop offset="0.55" stop-color="#c9c2b6"/>
        <stop offset="1" stop-color="#6e5a3c"/>
      </linearGradient>
    </defs>
    <line x1="17" y1="71" x2="115" y2="1" stroke="var(--teal)" stroke-width="3"/>
    <polygon points="382,150 184,295 382,295" fill="var(--teal)"/>
    <polygon points="309,180 382,128 382,138 312,189" fill="var(--blue)"/>
    <polygon points="150,295 382,295 382,539 160,539 55,385" fill="url(#bldg)" role="img" aria-label="Photo of a modern apartment building at dusk with trees and a street lamp"/>
    <polygon points="0,345 92,295 184,295 0,440" fill="var(--navy)"/>
    <polygon points="0,385 30,340 165,539 0,539" fill="var(--blue)"/>
    <polygon points="0,470 0,539 68,539" fill="var(--navy)"/>
  </svg>
  <div class="brand" style="left:196px; top:75px; width:204px; font-size:17px;">KEYSTONE</div>
  <h1 class="abs cover-title"><span class="t-act">ACT</span><span class="t-main">Maintenance</span><span class="t-plan">PLAN</span></h1>
  <div class="abs cover-rule"></div>
  <p class="abs cover-date">2 May 2022</p>
  <p class="abs cover-site">Units Plan1722<br>2 Sample Street Canberra City</p>
  <p class="abs cover-contact" style="left:183px;">Ph- 6211 0480<br>homefrontreports.example<br>hello@homefrontreports.example</p>
  <p class="abs cover-contact" style="left:304px;"><strong>Address</strong><br>18 Marlow Street<br>Hughes ACT 2605</p>
</section>

<!-- Page 2: report summary -->
<section class="page page--summary">
  <svg class="art" viewBox="0 0 382 539">
    <defs>
      <linearGradient id="site" x1="0" y1="0" x2="0" y2="1">
        <stop offset="0" stop-color="#7fc6f2"/>
        <stop offset="0.6" stop-color="#8aa0b4"/>
        <stop offset="1" stop-color="#6a5a50"/>
      </linearGradient>
      <linearGradient id="sketch" x1="0" y1="0" x2="1" y2="0">
        <stop offset="0" stop-color="#e8e8e8"/>
        <stop offset="1" stop-color="#c8ccd0"/>
      </linearGradient>
    </defs>
    <polygon points="0,0 106,0 106,267 0,307" fill="var(--navy)"/>
    <polygon points="0,320 106,284 106,311 0,348" fill="var(--blue)"/>
    <polygon points="0,361 106,325 106,539 0,539" fill="url(#site)" role="img" aria-label="Photo of a worker on scaffolding among steel reinforcing bars"/>
    <rect x="256" y="75" width="126" height="47" fill="url(#sketch)" role="img" aria-label="Sketch of a city skyline with cranes being drawn by hand"/>
    <path d="M289 510 C296 500 300 512 306 503 S318 506 330 506 L362 505" fill="none" stroke="#666" stroke-width="0.7"/>
  </svg>
  <h2 class="abs side-heading">REPORT<br>SUMMARY</h2>
  <p class="abs side-label side-label--scope">Project Scope:</p>
  <p class="abs side-label side-label--class">Building Class</p>
  <p class="abs side-note">-Residential Units are Class A</p>

  <div class="abs facts facts--a">
    <div class="row"><span class="k">CLIENT</span><span class="v">Northgate Strata Group Pty Ltd</span></div>
    <div class="row"><span class="k">BUILDING LOCATION</span><span class="v">2 Sample Street Canberra City ACT</span></div>
    <div class="row" style="width:116px"><span class="k" style="width:91px">BLOCK NUMBER</span><span class="v">13</span></div>
    <div class="row" style="width:116px"><span class="k" style="width:91px">SECTION NUMBER</span><span class="v">12</span></div>
    <div class="row" style="width:116px"><span class="k" style="width:91px">SCHEME NUMBER</span><span class="v">Up1722</span></div>
  </div>
  <div class="abs facts facts--b">
    <div class="row"><span class="k">INSPECTION DATE</span><span class="v">2 May 2022</span></div>
    <div class="row"><span class="k">INSPECTOR</span><span class="v">Liam Carver</span></div>
    <div class="row"><span class="k">WEATHER CONDITIONS</span><span class="v">Fine</span></div>
    <div class="row"><span class="k">REFERENCE NUMBER</span><span class="v">35TST</span></div>
  </div>

  <p class="abs body body--lead">This Maintenance Plan has been compiled to assist the Owners Corporation and Strata Managers to meet their obligations with respect to the following legislation (both as amended 1 November 2020):</p>
  <div class="abs bullets"><span>Unit Titles (Management) Act 2011 (s24);</span><span>Unit Titles (Management) Regulation 2011 (s4A)</span></div>
  <p class="abs body body--class">In typical Class A Units Plans, the unit owner owns the inside of the unit but not the main structure of the building. Usually, the individual owner owns from the inside of their lot to halfway out through the boundary walls, ceiling, and the floor. In general, the Owners Corporation owns the walls, ceiling and floor from outside of the lot to halfway in. The internal walls within the unit (e.g. the wall between the kitchen and lounge room), floor coverings, light fittings and curtains are all the property of the unit owner.</p>
  <p class="abs body body--act">The Unit Titles (Management) Act 2011 and associated regulations provides the framework for the management of multi-unit residential properties. All Owners Corporations are required to hold a Maintenance Plan, considering the Developers Maintenance Schedule (if available). The Executive Committee then references this plan as part of their responsibility for overseeing the maintenance of the common property. The Owners Corporation should regularly review their maintenance plan and amend when necessary. A comprehensive database relating to the maintenance, repair or replacement undertaken to systems, equipment, structures and other items on the common property, including copies of manuals and warranties (where available) has been compiled for this building.</p>
  <p class="abs body body--file">Following the preparation of our project file for 2 Sample Street Canberra which included referencing materials such as maintenance schedules, sinking fund reports, warranties, manufacturer's recommendations, and specific product information provided to us, our Building Inspector conducted a comprehensive on-site visual inspection on 2 May 2022. It is critical that this Maintenance Plan is monitored and updated on an ongoing basis to ensure the optimum working condition of systems, equipment, structures and other elements of the common property and to avoid costly reactive repairs.</p>
  <h3 class="abs important">IMPORTANT</h3>
  <p class="abs body body--important">This report is intended to be read in its entirety. It has been commissioned to satisfy the requirements of 4A Maintenance plan – Act, s 24 (3), Unit Titles Management Regulation 2011. The appropriate Strata Group Representative or Members of the Body Corporate Executive are requested to immediately contact our company if any of the report's content is not fully understood and requires clarification or further explanation. <em>Please refer to important Scope and Limitations at the end of this document.</em></p>
  <p class="abs thanks">Thank you for the opportunity to work with you on this project, please do not hesitate to contact our team.</p>
  <p class="abs signoff">Liam Carver<br>Senior Building Inspector</p>
</section>

<!-- Page 3: community and photo log -->
<section class="page page--community">
  <svg class="art" viewBox="0 0 382 539">
    <defs>
      <linearGradient id="city" x1="0" y1="0" x2="0" y2="1">
        <stop offset="0" stop-color="#f4f5f6"/>
        <stop offset="0.5" stop-color="#b9bcbf"/>
        <stop offset="1" stop-color="#7d8386"/>
      </linearGradient>
    </defs>
    <polygon points="72,0 382,0 382,124 300,172 160,90 72,38" fill="url(#city)" role="img" aria-label="Photo of a hand holding a miniature city with a crane above an aerial cityscape"/>
    <polygon points="42,17 192,103 42,192" fill="var(--blue)"/>
    <polygon points="382,43 231,130 382,219" fill="var(--teal)"/>
    <polygon points="225,160 356,236 356,150" fill="#e9ecec" opacity="0.7"/>
    <rect x="304" y="100" width="62" height="25" fill="#fff" stroke="#1e7a3a" stroke-width="1.2" role="img" aria-label="Industry association membership badge"/>
    <rect x="307" y="103" width="56" height="19" fill="#1e7a3a"/>
    <rect x="22" y="312" width="163" height="160" fill="#dfe8e0" role="img" aria-label="Street map of Canberra with the property circled"/>
    <rect x="196" y="312" width="162" height="160" fill="#4d5a4a" role="img" aria-label="Satellite view of Canberra with the property circled"/>
    <ellipse cx="62" cy="395" rx="19" ry="9" fill="none" stroke="#d21f1f" stroke-width="1"/>
    <ellipse cx="238" cy="396" rx="18" ry="9" fill="none" stroke="#d21f1f" stroke-width="1"/>
  </svg>
  <p class="abs charity-text">A percentage from every inspection contributes to our in house charity, supporting those in our community who do not have a place to call home. Visit our website to learn more.</p>
  <p class="abs charity-name">Open Door</p>
  <p class="abs photo-note">A comprehensive photo log of all photographs and documents captured during the maintenance plan inspection on 2 May 2022 have been supplied with this report.</p>
</section>

<!-- Page 4: terms of use -->
<section class="page page--terms">
  <svg class="art" viewBox="0 0 382 539">
    <defs>
      <linearGradient id="skyline" x1="0" y1="0" x2="1" y2="1">
        <stop offset="0" stop-color="#eef1f6"/>
        <stop offset="0.5" stop-color="#9db0d2"/>
        <stop offset="1" stop-color="#3e5a98"/>
      </linearGradient>
    </defs>
    <polygon points="139,0 382,0 382,152" fill="var(--teal)"/>
    <polygon points="70,127 258,22 382,150 382,324 250,262" fill="url(#skyline)" role="img" aria-label="Photo of an engineer holding a hard hat overlooking a city skyline and highway"/>
    <polygon points="99,144 131,159 99,177" fill="var(--blue)"/>
  </svg>
  <div class="brand" style="left:0; top:68px; width:142px; font-size:14px;">KEYSTONE</div>
  <h2 class="abs use-heading">This report is written solely<br>for the use and benefit of:</h2>
  <p class="abs use-item"><b>1.</b> Northgate Strata Group Pty Ltd, representing the Owners Corporation for 2 Sample Street Canberra City</p>
  <p class="abs valid">This report is valid on the date of inspection.</p>

  <p class="abs legal legal--l" style="top:320px;"><b>NO LIABILITY</b> or responsibility in contract or tort or statute is accepted to any <b>Other Party</b> who may rely on the report wholly or in part. Any <b>Other Party</b> acting or relying on this report, wholly or in part, does so at their own risk.</p>
  <p class="abs legal legal--r" style="top:320px;"><b>NO LIABILITY</b> shall be accepted where documents supplied by external agencies, the client or their representative, have any omissions, errors or are incomplete, inaccurate or illegible.</p>
  <p class="abs legal legal--l" style="top:379px;"><b>NO LIABILITY</b> or responsibility will be accepted if the invoice for this report is not settled.</p>
  <p class="abs legal legal--r" style="top:379px;">The report is only an opinion of Homefront Reports and is valid for one hundred and eighty (180) days from the date of inspection.</p>
  <p class="abs legal legal--l" style="top:419px;">If it is claimed that there is any other omission relating to this report, Homefront Reports must be notified in writing before <b>ANY</b> action is taken. <b>NO LIABILITY</b> shall be accepted where any costs (including for remedial action or professional advice) are incurred prior to Homefront Reports receiving written notification.</p>
  <p class="abs legal legal--r" style="top:419px;">This report supersedes any other report, verbal or written, given to you by this company in respect of this property. If you have questions or do not understand any part of this document and require clarification, please contact our inspector prior to acting on this report.</p>
  <p class="abs copyright">© Copyright remains with Homefront Reports, the report content, style and presentation is not to be copied<br>or reproduced without written authority of the Company.</p>
</section>

</body>
</html>
```